Bref créative |
Website for Kelp Harbour | ||
Kelp Harbour | ||
Massage Therapy | ||
www.kelpharbour.co.uk (not live yet) | ||
Friendly and professional mobile massage therapy company. Offer a range of massage types such as holistic, remedial, deep tissue and sports. Also offer postural assessments, range of movement and joint tests Work with corporate and private clients, sports teams and charities |
Dislike....Anything too masculine or too feminine Too much clutter on web pages Imbalance between amount of text and images To much industry speak Like...plenty of white space positive and energetic text and images clear and concise text, without jargon Making clients feel comfortable and the company feel approachable |
Cutting-Edge Unique/Creative Clean/Simple Professional Trendy Friendly Exciting Modern Colorful Elegant |
White | ||
Dark Blue/Indigo | ||
Light/Mint Green | ||
top | ||
http://www.quorvastudio.com/ | ||
http://plw-tandor.com/ | ||
http://www.vestoria.co.uk/spa.html | ||
• Additional Comments were - I like QuorvaStudio use of white space and their balance between text and images. They also use Plain English which i think makes clients comfortable and they appear approachable. Vestoria Spa feels very elegant in its design and I like the simple navigation. PLW Tandor I like the way in they break information down about massage itself, making it easy to read and digest. Their actual design though I think could be better. • Logo and contact details are to appear on every page |

```html
<!DOCTYPE html>
<html lang="en">
<head>
<meta charset="utf-8">
<title>Kelp Harbour — Massage Therapy</title>
<link href="https://fonts.googleapis.com/css2?family=Montserrat:wght@700&family=Questrial&display=swap" rel="stylesheet">
<style>
  :root {
    --navy: #1d3557;
    --navy-deep: #142a47;
    --mint: #8fcfb0;
    --mint-light: #cfeedd;
    --mint-nav: #7fb9a0;
    --white: #ffffff;
    --grey-text: #666b70;
    --skin-light: #f2d2bf;
    --skin-mid: #d9a88e;
    --skin-dark: #8a5a48;
  }
  * { box-sizing: border-box; margin: 0; padding: 0; }
  html, body { width: 1200px; height: 840px; overflow: hidden; }
  body {
    position: relative;
    font-family: "Questrial", "Century Gothic", sans-serif;
    background: linear-gradient(to bottom, var(--white) 0%, var(--white) 68%, var(--mint-light) 100%);
    color: var(--navy);
  }
  .brand { position: absolute; left: 149px; top: 24px; }
  .brand-name {
    display: flex; align-items: center; gap: 14px;
    font-family: "Montserrat", sans-serif; font-weight: 700;
    font-size: 50px; line-height: 1; color: var(--navy); letter-spacing: -0.5px;
  }
  .brand-dot { width: 22px; height: 22px; border-radius: 50%; background: var(--mint); }
  .brand-tagline {
    margin-top: 12px; font-size: 22px; letter-spacing: 1.5px; color: var(--mint-nav);
  }
  .contact { position: absolute; left: 792px; top: 94px; font-size: 17px; color: var(--navy); line-height: 26px; }
  .contact-row { display: flex; align-items: center; gap: 8px; }
  .contact-row svg { width: 14px; height: 14px; }

  .stage {
    position: absolute; left: 137px; top: 158px; width: 926px; height: 598px;
    border: 2px solid #d4d8da; box-shadow: 0 6px 18px rgba(0,0,0,0.18);
    overflow: hidden;
  }
  .stage-photo {
    position: absolute; inset: 0;
    background:
      radial-gradient(ellipse 420px 300px at 760px 420px, var(--skin-light) 0%, var(--skin-mid) 55%, transparent 100%),
      linear-gradient(100deg, #4a3a36 0%, #6d5148 35%, var(--skin-mid) 70%, var(--skin-dark) 100%);
  }
  .nav {
    position: absolute; left: 0; top: 0; right: 0; height: 48px;
    background: linear-gradient(to bottom, rgba(170,220,195,0.92), rgba(120,180,155,0.92));
    display: flex; align-items: center; padding-left: 140px;
  }
  .nav a {
    color: var(--white); text-decoration: none; font-size: 19px; padding: 0 14px;
    border-right: 1px solid rgba(255,255,255,0.7); line-height: 20px;
  }
  .nav a:last-child { border-right: none; }
  .intro {
    position: absolute; left: 40px; top: 82px; width: 560px;
    color: var(--white); font-size: 18px; line-height: 23px;
  }
  .intro-rule { position: absolute; left: 220px; top: 302px; width: 200px; height: 1px; background: rgba(255,255,255,0.6); }
  .card { position: absolute; left: 42px; width: 540px; height: 118px; }
  .card-massage { top: 280px; }
  .card-assess { top: 442px; }
  .card-photo {
    position: absolute; left: 0; top: 0; width: 252px; height: 118px;
    border: 2px solid var(--white);
  }
  .card-massage .card-photo { background: linear-gradient(120deg, #f6e1d3, var(--skin-mid) 70%, #b98670); }
  .card-assess .card-photo { background: linear-gradient(120deg, #e8e2dd, #c9b3a7 60%, #9c8478); }
  .card-label {
    position: absolute; left: 102px; top: -14px; background: var(--navy-deep); color: var(--white);
    font-family: "Montserrat", sans-serif; font-weight: 700; font-size: 15px;
    padding: 6px 10px; white-space: nowrap;
  }
  .card-text {
    position: absolute; left: 262px; top: 52px; width: 280px; height: 66px;
    background: rgba(120,100,100,0.55); color: var(--white);
    font-size: 13px; line-height: 15px; padding: 4px 8px;
  }
  .card-text strong { font-family: "Montserrat", sans-serif; font-size: 12px; }
  .footer {
    position: absolute; top: 797px; left: 0; width: 1200px; text-align: center;
    font-size: 14px; color: var(--grey-text); padding-left: 10px;
  }
</style>
</head>
<body>
  <header class="brand">
    <div class="brand-name">Kelp Harbour <span class="brand-dot"></span></div>
    <div class="brand-tagline">Re-balance and Re-energise</div>
  </header>

  <div class="contact">
    <div class="contact-row">
      <svg viewBox="0 0 14 14"><rect x="3" y="1" width="8" height="12" rx="1.5" fill="var(--mint)"/><rect x="5" y="3" width="4" height="6" fill="var(--white)"/></svg>
      <span>07700 900418</span>
    </div>
    <div class="contact-row">
      <svg viewBox="0 0 14 14"><rect x="1" y="3" width="12" height="8" fill="var(--mint)"/><polyline points="1,3 7,8 13,3" fill="none" stroke="var(--white)" stroke-width="1.2"/></svg>
      <span>hello@kelpharbour.co.uk</span>
    </div>
  </div>

  <main class="stage">
    <div class="stage-photo" role="img" aria-label="Close-up of a relaxed client receiving a shoulder massage"></div>
    <nav class="nav">
      <a href="#">Home</a><a href="#">About</a><a href="#">What to Expect</a><a href="#">Prices and Times</a><a href="#">Testimonials</a>
    </nav>
    <p class="intro">Kelp Harbour isn’t just about a good massage. Kelp Harbour will help re-balance and re-energise, not only you but your entire life. We offer a wide range of different massages, postural assessments, range of movement and joint tests to get you back to being balanced and feeling good in your own body. We work with everyone from private and corporate clients, sports teams, and even charities.</p>
    <div class="intro-rule"></div>

    <section class="card card-massage">
      <div class="card-photo" role="img" aria-label="Client relaxing during a massage treatment"></div>
      <h2 class="card-label">Types of Massage</h2>
      <p class="card-text">Lorem ipsum dolor sit amet, con-sectetur adipiscing elit. Curabitur accumsan lacus a metus volutpat eget aliquam elit iaculis...<br><strong>Learn More</strong></p>
    </section>

    <section class="card card-assess">
      <div class="card-photo" role="img" aria-label="Therapist carrying out a postural assessment"></div>
      <h2 class="card-label">Postural &amp; Joint Assessments</h2>
      <p class="card-text">Lorem ipsum dolor sit amet, con-sectetur adipiscing elit. Curabitur accumsan lacus a metus volutpat eget aliquam elit iaculis...<br><strong>Learn More</strong></p>
    </section>
  </main>

  <footer class="footer">© Copyright 2012 Kelp Harbour</footer>
</body>
</html>
```